New Zealand Marlborough Sauvignon Blanc wine packaging design

We need packaging design for our new wine brand, Dunmore Hale. The wine is a New Zealand Marlborough Sauvignon Blanc. We would like the packaging will portray elegance and style with an understated label. We are looking for a label that portrays the elegance of the French Riviera. The label should be round or pill shaped.
Updates

Industry/Entity Type

Wine

Font styles to use
Serif
Sans Serif

Requirements
Must have
• The words in order of importance: Dunmore Hale, Sauvignon Blanc, Marlborough, New Zealand. It should be fit to the bottle posted in the links
Nice to have
• a pill shape or circular shape
Should not have
• Illustrations of wine bottles, wine glasses, or grapes

```html
<!DOCTYPE html>
<html lang="en">
<head>
<meta charset="utf-8">
<title>Dunmore Hale Sauvignon Blanc – Label</title>
<link rel="stylesheet" href="https://fonts.googleapis.com/css2?family=Playfair+Display:wght@900&family=Cinzel:wght@400&display=swap">
<style>
  :root {
    --page: #ffffff;
    --label-grey: #8b8d90;
    --ornament-grey: #979a9d;
    --teal: #07778c;
    --teal-soft: #1a8598;
    --white: #ffffff;
  }
  * { box-sizing: border-box; margin: 0; padding: 0; }
  html, body {
    width: 1200px;
    height: 675px;
    overflow: hidden;
    background: var(--page);
  }
  .canvas {
    position: relative;
    width: 1200px;
    height: 675px;
  }
  .label {
    position: absolute;
    left: 390px;
    top: 44px;
    width: 420px;
    height: 587px;
    border-radius: 210px / 210px;
    background: var(--label-grey);
    overflow: hidden;
  }
  .label__panel {
    position: absolute;
    left: 32px;
    top: 30px;
    width: 357px;
    height: 366px;
    border-radius: 178px 178px 0 0 / 168px 168px 0 0;
    background: var(--teal);
  }
  .label__frame-ornament {
    position: absolute;
    inset: 0;
    width: 357px;
    height: 366px;
  }
  .label__base-ornament {
    position: absolute;
    left: 46px;
    top: 396px;
    width: 328px;
    height: 175px;
    border-radius: 0 0 164px 164px / 0 0 140px 140px;
    background: radial-gradient(ellipse at 50% 30%, var(--label-grey) 35%, var(--ornament-grey) 100%);
  }
  .brand {
    position: absolute;
    left: 0;
    width: 420px;
    top: 200px;
    text-align: center;
    font-family: "Playfair Display", Georgia, serif;
    font-weight: 900;
    font-size: 56px;
    line-height: 42px;
    color: var(--white);
    letter-spacing: -0.5px;
  }
  .brand span { display: block; }
  .varietal {
    position: absolute;
    left: 0;
    width: 420px;
    top: 320px;
    text-align: center;
    font-family: "Cinzel", "Times New Roman", serif;
    font-size: 22px;
    line-height: 26px;
    color: var(--white);
    letter-spacing: 0.5px;
  }
  .region {
    position: absolute;
    left: 0;
    width: 420px;
    top: 413px;
    text-align: center;
    font-family: "Cinzel", "Times New Roman", serif;
    font-size: 12.5px;
    line-height: 14px;
    color: var(--teal);
    letter-spacing: 0.3px;
  }
  .region span { display: block; }
</style>
</head>
<body>
  <main class="canvas">
    <section class="label" aria-label="Dunmore Hale Sauvignon Blanc wine label">
      <div class="label__panel">
        <svg class="label__frame-ornament" viewBox="0 0 357 366" role="img" aria-label="Fine swirling filigree ornament framing the arch">
          <path d="M6 366 V170 A172 164 0 0 1 351 170 V366 H302 V180 A124 120 0 0 0 55 180 V366 Z" fill="var(--teal-soft)"/>
        </svg>
      </div>
      <div class="label__base-ornament" role="img" aria-label="Swirling filigree ornament around the lower label"></div>

      <h1 class="brand"><span>Dunmore</span><span>Hale</span></h1>
      <p class="varietal">Sauvignon Blanc</p>
      <p class="region"><span>Marlborough,</span><span>New Zealand</span></p>
    </section>
  </main>
</body>
</html>
```